Business Card

Need a clean, professional, simple, but clever business card for our company LUX RIDES. We only want to see black and white colors as that reflects the branding of our company. Attaching logo. Will also consider the "sky blue" shown in our web site sample png - but use of the color should be minimal.

Lux Rides is a executive car service operating in cities throughout Africa. By operating well equipped Valdren Oster vehicles, we offer the smoothest and stylish ride in town. We aim to provide customers with a valuable experience. That’s why we make sure our patrons get picked up like a boss, travel in style, and Travel Refined.

We need a card that says that. Likely to print on the best quality/smoothest paper available, as it must speak volumes of our business and class.

We would like the rear of the card to be all black. Perhaps we can put the web url on it, or leave it blank if it looks neater/more elegant.

Use the following contact information (as you see fit):

Lux Rides Limited
P.O. Box 47106
Dar es Salaam, Tanzania

Baraka Kilonzo
Managing Director

+255 (0) 754 829016
sales@luxrides-demo.co.tz

web url: www.luxrides-demo.co.tz
email: chauffeur@luxrides-demo.co.tz

***Winning designer will likely be commissioned for more promotional work in near future.

Target Market(s)

The target market for this card is corporate executives of top firms (financial, consulting, businessmen, etc). They are interested in high quality transportation. Our fleet is all high end Valdren Oster black cars (black exterior, black interior); and therefore, that high end quality and promptness must be reflected in the card. Also simplicity, as we we take care of all the little details behind the scene.

Industry/Entity Type

Business

Requirements
Must have
• Font must be: Helvetica Neue, like the logo. You may use other variations (Thin, Ultra thin, Regular, Bold), so long as it looks and prints well.

If web url is included on the back of the card, then do NOT include it also on the front.
Nice to have
• If there is something nice and clever that you can do/think of that doesn't make the card look busy, but adds a little "posh", then I could be even more interested.

However, if there's no little thing do be done, I'd rather a simple, but very professional looking card that attracts a lot of attention.

```html
<!DOCTYPE html>
<html lang="en">
<head>
<meta charset="utf-8">
<title>Lux Rides — Business Card</title>
<link rel="stylesheet" href="https://fonts.googleapis.com/css2?family=Inter:wght@200;300;400;700&display=swap">
<style>
  :root {
    --backdrop: #3a3430;
    --card-black: #121212;
    --card-white: #ffffff;
    --ink: #1c1c1c;
    --ink-soft: #3a3a3a;
    --sky-blue: #1aa3c9;
    --edge-band: #1a1a1a;
  }
  * { margin: 0; padding: 0; box-sizing: border-box; }
  html, body {
    width: 1200px;
    height: 716px;
    overflow: hidden;
    background: var(--backdrop);
    font-family: "Inter", "Helvetica Neue", Arial, sans-serif;
  }
  .canvas {
    position: relative;
    width: 1200px;
    height: 716px;
    display: flex;
    align-items: center;
    justify-content: center;
    gap: 40px;
  }
  .card {
    position: relative;
    width: 520px;
    height: 297px;
    border-radius: 2px;
    overflow: hidden;
  }

  /* Back of card */
  .card-back { background: var(--card-black); }
  .card-back .brand-block {
    position: absolute;
    left: 150px;
    top: 112px;
  }
  .card-back .wordmark {
    color: var(--card-white);
    font-size: 40px;
    font-weight: 300;
    letter-spacing: 1px;
    line-height: 1;
  }
  .card-back .tagline {
    margin-top: 6px;
    color: var(--sky-blue);
    font-size: 17px;
    font-weight: 300;
  }

  /* Front of card */
  .card-front { background: var(--card-white); color: var(--ink); }
  .card-front .edge-band {
    position: absolute;
    right: 0;
    top: 0;
    width: 18px;
    height: 100%;
    background: var(--edge-band);
  }
  .card-front .wordmark {
    position: absolute;
    left: 34px;
    top: 46px;
    font-size: 38px;
    font-weight: 300;
    letter-spacing: 1px;
    line-height: 1;
    color: var(--ink);
  }
  .card-front .website {
    position: absolute;
    left: 36px;
    top: 178px;
    font-size: 14px;
    font-weight: 400;
    letter-spacing: 2px;
    color: var(--ink-soft);
  }
  .card-front .website .domain {
    color: var(--sky-blue);
    font-weight: 700;
  }
  .card-front .contact {
    position: absolute;
    left: 290px;
    top: 102px;
    font-size: 13px;
    font-weight: 300;
    line-height: 1.3;
    color: var(--ink-soft);
  }
  .contact .person-name {
    font-size: 16px;
    font-weight: 700;
    color: var(--ink);
  }
  .contact .person-title {
    font-size: 11px;
    font-weight: 400;
    letter-spacing: 0.3px;
    text-transform: uppercase;
    margin-bottom: 14px;
  }
  .contact .lines { margin-bottom: 12px; }
  .contact .company-name {
    font-weight: 700;
    color: var(--ink);
  }
</style>
</head>
<body>
<main class="canvas">
  <section class="card card-back" aria-label="Card back">
    <div class="brand-block">
      <div class="wordmark">LUX RIDES</div>
      <div class="tagline">Travel Refined.</div>
    </div>
  </section>

  <section class="card card-front" aria-label="Card front">
    <div class="wordmark">LUX RIDES</div>
    <div class="website">www.<span class="domain">luxrides-demo</span>.co.tz</div>
    <div class="contact">
      <div class="person-name">Baraka Kilonzo</div>
      <div class="person-title">Managing Director</div>
      <div class="lines">
        +255 (0) 754 829016<br>
        sales@luxrides-demo.co.tz<br>
        chauffeur@luxrides-demo.co.tz
      </div>
      <div class="company-name">Lux Rides Limited</div>
      <div>P.O. Box 47106</div>
      <div>Dar es Salaam, Tanzania</div>
    </div>
    <div class="edge-band"></div>
  </section>
</main>
</body>
</html>
```